Silver Heron Motor Works needs a logo design

I'm after a logo design for a new Female owned automotive repair workshop in the Queanbeyan/Canberra Australia Area.
We offer repairs on all passenger cars, 4wds and light trucks emphasising a strong honest work ethic and a genuine interest in the customer and their vehicles needs. With business details on the front of the card and what we offer on the back.
I would like a design with a phoenix in multiple colours maybe hovering over a flaming wheel or a car with wheels flaming with the phoenix hovering up out of the flames
Target Market(s)
All Vehicle users
Industry/Entity Type
Automotive
Contact Information for Business Card
On the front
Silver Heron Motor
Marla Pettigrew Owner/ Mechanic 0471385026
email marla@silverheronmotor.com.au
Website www.silverheronmotorworks.com.au
On the back
All Cars, 4WDs, Light trucks, makes and models
Log book servicing
General vehicle servicing
Major vehicle servicing
brake and clutch servicing and repairs
Suspension repairs
cooling systems
All major and minor mechanical repairs
minor electrical rewiring and repairs
Colors
Designer to choose colors to be used in the design.
Look and feel

```html
<!DOCTYPE html>
<html lang="en">
<head>
<meta charset="utf-8">
<title>Silver Heron Motor — Business Card</title>
<link href="https://fonts.googleapis.com/css2?family=Old+Standard+TT:wght@400;700&display=swap" rel="stylesheet">
<style>
  :root {
    --page: #e9e6e1;
    --card: #050505;
    --ink: #f1e6cf;
    --ink-soft: #d9ccb0;
    --flame-deep: #6e1c06;
    --flame: #c2410c;
    --flame-hot: #e8771c;
    --steel: #2a2a2c;
  }
  * { box-sizing: border-box; margin: 0; padding: 0; }
  html, body { width: 1200px; height: 1200px; overflow: hidden; }
  body {
    background: var(--page);
    font-family: "Old Standard TT", "Times New Roman", serif;
    display: flex;
    flex-direction: column;
    align-items: center;
    justify-content: center;
    gap: 40px;
  }
  .card {
    position: relative;
    width: 960px;
    height: 548px;
    background: var(--card);
    overflow: hidden;
    box-shadow: 0 10px 24px rgba(0,0,0,.25);
  }

  /* Back: services */
  .card-back .artwork {
    position: absolute;
    left: 130px; top: 90px;
    width: 720px; height: 380px;
    background: radial-gradient(ellipse at 50% 55%, rgba(194,65,12,.55) 0%, rgba(110,28,6,.4) 45%, rgba(5,5,5,0) 72%);
  }
  .services {
    position: absolute;
    inset: 0;
    display: flex;
    flex-direction: column;
    justify-content: center;
    align-items: center;
    gap: 22px;
    color: var(--ink);
    font-size: 23px;
    text-align: center;
    text-shadow: 0 1px 3px rgba(0,0,0,.8);
  }

  /* Front: contact */
  .card-front .artwork {
    position: absolute;
    right: 40px; top: 60px;
    width: 440px; height: 440px;
    border-radius: 50%;
    background: radial-gradient(circle at 50% 50%, var(--steel) 0%, #1a1410 40%, rgba(110,28,6,.45) 62%, rgba(5,5,5,0) 72%);
  }
  .brand {
    position: absolute;
    left: 120px; top: 200px;
    display: flex;
    align-items: center;
    gap: 26px;
  }
  .brand-mark {
    width: 70px; height: 70px;
    border-radius: 50%;
    background: var(--flame-hot);
  }
  .brand-name {
    color: var(--ink);
    font-size: 46px;
    line-height: 1.08;
    letter-spacing: 1px;
    text-transform: uppercase;
  }
  .brand-name span { display: block; }
  .brand-name span:nth-child(2) { padding-left: 24px; }
  .brand-name span:nth-child(3) { padding-left: 48px; }
  .divider {
    position: absolute;
    left: 505px; top: 165px;
    width: 1px; height: 215px;
    background: var(--ink-soft);
  }
  .contact {
    position: absolute;
    left: 530px; top: 175px;
    color: var(--ink);
  }
  .contact-name { font-size: 40px; line-height: 1.1; }
  .contact-role { font-size: 21px; color: var(--ink-soft); margin: 6px 0 34px 20px; }
  .contact-line {
    display: flex;
    align-items: center;
    gap: 14px;
    font-size: 22px;
    margin-left: 38px;
    margin-bottom: 10px;
  }
  .contact-line svg { width: 24px; height: 24px; flex: none; }
</style>
</head>
<body>

  <section class="card card-back" aria-label="Card back: services">
    <div class="artwork" role="img" aria-label="Dark photo of a sports car engulfed in orange flames"></div>
    <div class="services">
      <p>All Cars, 4wds, Light Trucks, Makes And Models</p>
      <p>Log Book Servicing | General Vehicle Servicing | Major Vehicle Servicing</p>
      <p>Brake And Clutch Servicing And Repairs | Suspension Repairs | Cooling Systems</p>
      <p>All Major And Minor Mechanical Repairs | Minor Electrical Rewiring And Repairs</p>
    </div>
  </section>

  <section class="card card-front" aria-label="Card front: contact details">
    <div class="artwork" role="img" aria-label="Faint alloy car wheel wrapped in flames"></div>
    <div class="brand">
      <div class="brand-mark"></div>
      <h1 class="brand-name"><span>Silver</span><span>Heron</span><span>Motor</span></h1>
    </div>
    <div class="divider"></div>
    <div class="contact">
      <p class="contact-name">Marla Pettigrew</p>
      <p class="contact-role">Owner/ Mechanic</p>
      <p class="contact-line">
        <svg viewBox="0 0 24 24" aria-hidden="true"><path fill="#f1e6cf" d="M6.6 10.8a15.1 15.1 0 0 0 6.6 6.6l2.2-2.2c.3-.3.7-.4 1-.2 1.1.4 2.3.6 3.6.6.6 0 1 .4 1 1V20c0 .6-.4 1-1 1A17 17 0 0 1 3 4c0-.6.4-1 1-1h3.5c.6 0 1 .4 1 1 0 1.3.2 2.5.6 3.6.1.3 0 .7-.2 1z"/></svg>
        0471385026
      </p>
      <p class="contact-line">
        <svg viewBox="0 0 24 24" aria-hidden="true"><rect x="2" y="5" width="20" height="14" fill="#f1e6cf"/><path d="M2 5l10 8 10-8" fill="none" stroke="#050505" stroke-width="1.6"/></svg>
        marla@silverheronmotor.com.au
      </p>
    </div>
  </section>

</body>
</html>
```